TOLVANE WEBSITE

We need a new look for our current website. Tolvane Fast Debt Recovery have been in business since 1977. We want our logo to remain the same however our current website is cluttered and we want something fresh, uncluttered, clean-line and easy to use. Our company colours are red, white and black.
We don't want pictures of people across the top of the page instead, we would like messages to appear (scrolling) across the top on a red background with white writing.
All that is required is from the designer to create a new look home page.
Good afternoon designers,
I have attached another page to the Tolvane Website profile. Could you please take a look and word towards creating something which incorporates the blue box.
I look forward to receiving your designs.
Thanks
Neil

```html
<!DOCTYPE html>
<html lang="en">
<head>
<meta charset="utf-8">
<title>Tolvane Fast Debt Recovery</title>
<link href="https://fonts.googleapis.com/css2?family=Lato:wght@400;700;900&family=Arimo:wght@400;700&display=swap" rel="stylesheet">
<style>
:root{
  --page-bg:#303032;
  --white:#ffffff;
  --ink:#111111;
  --red:#d0101a;
  --red-dark:#7a0008;
  --red-bright:#f0202a;
  --grey-text:#a9a9a9;
  --rule:#e6e6e6;
}
*{margin:0;padding:0;box-sizing:border-box}
html,body{width:1040px;height:1200px;overflow:hidden;background:var(--page-bg)}
body{position:relative;font-family:'Lato',sans-serif;color:var(--white)}
.abs{position:absolute}

/* header */
.logo-box{left:147px;top:0;width:151px;height:96px;background:var(--white);display:flex;flex-direction:column;align-items:center;justify-content:center;padding-top:4px}
.logo-name{font-weight:900;font-size:30px;color:var(--ink);letter-spacing:-1px;line-height:1}
.logo-tag{font-size:8px;font-weight:700;color:var(--ink);letter-spacing:2.4px;margin-top:5px;border-top:1.5px solid var(--ink);border-bottom:1.5px solid var(--ink);padding:1px 0}
.logo-sub{font-size:6.5px;font-weight:700;color:var(--ink);letter-spacing:1.6px;margin-top:2px}
.call-now{right:147px;top:7px;text-align:right;padding-right:16px;line-height:1.15}
.call-now .label{font-size:14px}
.call-now .number{font-size:15px;font-weight:700}
.call-now svg{position:absolute;right:0;top:2px}
.main-nav{left:323px;top:66px;display:flex;align-items:center;font-size:9.5px;font-weight:700;text-transform:uppercase;letter-spacing:-.3px;white-space:nowrap}
.main-nav span{padding:0 7px;border-left:1px solid var(--white);line-height:10px}
.main-nav span:last-child{padding:0;width:0}
.main-nav .active{background:var(--white);color:var(--ink);padding:6px 6px;border-left:none;margin:0 3px;line-height:11px}

/* banner */
.banner{left:147px;top:109px;width:523px;height:191px;border:1px solid #8b0b12;overflow:hidden;
  background:radial-gradient(ellipse at 75% 20%,var(--red-bright) 0%,var(--red) 35%,transparent 70%),
  linear-gradient(160deg,var(--red-dark) 0%,var(--red) 45%,#a4000c 70%,#5e0006 100%)}
.banner h1{position:absolute;left:11px;top:12px;font-size:22px;font-weight:900;line-height:24px;letter-spacing:-1.2px;text-transform:uppercase}
.banner p{position:absolute;left:11px;top:88px;font-size:12px;line-height:15px}
.banner .more{position:absolute;right:22px;bottom:7px;font-size:10.5px}
.banner .pager{position:absolute;left:11px;bottom:11px;display:flex;gap:1px}
.banner .pager i{width:16px;height:16px;background:#eee;display:flex;align-items:center;justify-content:center;font-style:normal;color:#444;font-size:7px}

/* side menu */
.side-menu{left:691px;top:109px;width:202px}
.side-menu div{height:29px;margin-bottom:3px;font-family:'Arimo',sans-serif;font-size:17px;padding-left:9px;line-height:30px;color:var(--grey-text);
  background:linear-gradient(#909090,#6a6a6a);border-bottom:2px solid #222}
.side-menu .current{background:linear-gradient(#ffffff,#e2e2e2);color:var(--ink)}

/* headings & text */
.sec-title{font-size:19px;font-weight:700;line-height:24px;padding-bottom:3px;border-bottom:1px solid var(--rule);white-space:nowrap}
.body-text{font-size:10px;line-height:13px}
.service-pic{width:163px;height:117px}
.service-title{font-size:12px;font-weight:700;line-height:14px;width:165px}
.service-text{font-size:9.5px;line-height:12px;width:165px}
.action{width:170px;text-align:center}
.action .name{font-size:19px;font-weight:700;line-height:22px}
.action .sub{font-size:10.5px;font-weight:700}
.action svg{display:block;margin:0 auto 4px}

/* side */
.photo-card{left:691px;top:455px;width:202px;height:136px;background:linear-gradient(135deg,#c9c9cd,#7d7a80 50%,#2a2628)}
.photo-card .caption{position:absolute;left:4px;bottom:3px;font-size:18px;font-weight:700;color:var(--white)}
.promo{left:691px;top:612px;width:202px;height:426px;overflow:hidden;background:linear-gradient(90deg,#f4f4f4 0%,#e8e3df 40%,#9a7a66 75%,#4a3a34 100%)}
.promo .lines{position:absolute;left:50px;bottom:127px;width:300px;height:42px;transform-origin:0 100%;transform:rotate(-90deg);white-space:nowrap}
.promo .l1,.promo .l2{font-size:21px;font-weight:900;line-height:21px;text-transform:uppercase;letter-spacing:-.5px}
.promo .l1{color:var(--red)}
.promo .l2{color:var(--ink)}

/* footer */
.footer-rule{left:147px;top:1075px;width:746px;border-top:1px solid var(--rule)}
.footer-nav{left:0;width:1040px;top:1087px;display:flex;justify-content:center;gap:19px;font-size:9.5px}
.copyright{left:0;width:1040px;top:1111px;text-align:center;font-size:9.5px}
</style>
</head>
<body>

<header>
  <div class="abs logo-box">
    <div class="logo-name">TOLVANE</div>
    <div class="logo-tag">FAST DEBT RECOVERY</div>
    <div class="logo-sub">NO RECOVERY - NO CHARGE</div>
  </div>

  <div class="abs call-now">
    <div class="label">Call us now :</div>
    <div class="number">0844 555 0192</div>
    <svg width="12" height="38" viewBox="0 0 12 38"><path d="M3 2 C10 3 11 27 3 30" stroke="#fff" stroke-width="3.5" fill="none" stroke-linecap="round"/><path d="M6 32 q-2 3 0 5" stroke="#fff" stroke-width="1" fill="none"/></svg>
  </div>

  <nav class="abs main-nav">
    <span class="active">Home</span><span>About us</span><span>Rates</span><span>Products &amp; Solution</span><span>Media Centre</span><span>Careers</span><span>Contact us</span><span>Client Login</span><span></span>
  </nav>
</header>

<section class="abs banner">
  <h1>We guarantee to<br>collect your overdue<br>accounts better than anyone else.</h1>
  <p>Because if we don't collect,<br>we don't get paid.</p>
  <div class="pager"><i>◀</i><i>▶</i></div>
  <div class="more">Find out how we can help you...</div>
</section>

<nav class="abs side-menu">
  <div class="current">Harrowgate Lawyers</div>
  <div>Submit a Debt</div>
  <div>Corporate Clients</div>
  <div>Small Business</div>
  <div>Make a Payment</div>
  <div>Forms</div>
</nav>

<main>
  <h2 class="abs sec-title" style="left:146px;top:318px;width:292px">First choice for Debt Collection</h2>
  <div class="abs body-text" style="left:148px;top:360px;width:510px">
    Lorem Ipsum is simply dummy text of the printing and typesetting industry. Lorem Ipsum has been the industry's standard dummy text ever since the 1500s, when an unknown printer took a galley of type and scrambled it to make a type specimen book. It has survived not only five centuries, but also the leap into electronic typesetting, remaining essentially unchanged. It was popularised in the 1960s with the release of Letraset sheets containing Lorem Ipsum passages, and more recently with desktop publishing software like Aldus PageMaker including versions of Lorem Ipsum.<br>
    Lorem Ipsum is simply dummy text of the printing and typesetting industry. Lorem Ipsum has been the industry's standard dummy text ever since the 1500s, when an unknown printer took a galley of type and scrambled it to make a type specimen book. It has survived not only five centuries, but also the leap into electronic typesetting, remaining essentially unchanged.
  </div>

  <div class="abs service-pic" role="img" aria-label="Red overdue rubber stamp on white" style="left:147px;top:507px;background:linear-gradient(160deg,#fff 20%,#b93a3a 45%,#fff 75%)"></div>
  <div class="abs service-pic" role="img" aria-label="Rising bar chart with red arrow" style="left:319px;top:507px;background:linear-gradient(160deg,#fff 30%,#d6d8dc 60%,#f4f4f4)"></div>
  <div class="abs service-pic" role="img" aria-label="Red globe on white" style="left:492px;top:507px;background:radial-gradient(circle at 50% 55%,#e02828 0,#e02828 30%,#fff 32%)"></div>

  <div class="abs service-title" style="left:147px;top:637px">Commercial Debt Collection</div>
  <div class="abs service-title" style="left:319px;top:637px">Private &amp; Consumer Debt Collection</div>
  <div class="abs service-title" style="left:492px;top:637px">International Debt Collection</div>

  <div class="abs service-text" style="left:147px;top:676px">Lorem Ipsum is simply dummy text of the printing and typesetting industry.</div>
  <div class="abs service-text" style="left:319px;top:676px">Lorem Ipsum is simply dummy text of the printing and typesetting industry.</div>
  <div class="abs service-text" style="left:492px;top:677px">Lorem Ipsum is simply dummy text of the printing and typesetting industry.</div>

  <h2 class="abs sec-title" style="left:146px;top:727px;width:238px">Call us on 0844 555 0192
    <svg width="17" height="15" viewBox="0 0 17 15" style="vertical-align:-1px"><path d="M1 5 Q8.5 -1 16 5 L13 7 L11 5 L6 5 L4 7 Z" fill="#fff"/><rect x="3" y="8" width="11" height="6" rx="1.5" fill="#fff"/><circle cx="8.5" cy="11" r="1.6" fill="#303032"/></svg>
  </h2>

  <div class="abs action" style="left:129px;top:780px">
    <svg width="78" height="68" viewBox="0 0 78 68">
      <g fill="#c9cbcf" stroke="#8b8d91" stroke-width="1">
        <circle cx="28" cy="22" r="17"/><circle cx="52" cy="44" r="20"/><circle cx="22" cy="50" r="13"/>
      </g>
      <g fill="#555"><circle cx="28" cy="22" r="6"/><circle cx="52" cy="44" r="7"/><circle cx="22" cy="50" r="4.5"/></g>
    </svg>
    <div class="name">Other Services</div><div class="sub">More services we can offer</div>
  </div>
  <div class="abs action" style="left:317px;top:780px">
    <svg width="60" height="68" viewBox="0 0 60 68"><text x="30" y="62" text-anchor="middle" font-family="Lato,sans-serif" font-weight="900" font-size="74" fill="#e4e4e6">?</text></svg>
    <div class="name">Enquire Now!</div><div class="sub">Fill in our quick enquiry form</div>
  </div>
  <div class="abs action" style="left:497px;top:780px">
    <svg width="70" height="68" viewBox="0 0 70 68"><path d="M8 56 L35 40 L64 54 L37 68 Z" fill="#e8e8e8"/><rect x="20" y="26" width="30" height="28" rx="6" fill="#2a2a2a"/><rect x="20" y="34" width="30" height="3" fill="#666"/><rect x="20" y="43" width="30" height="3" fill="#666"/><rect x="32" y="6" width="6" height="22" fill="#333"/><circle cx="35" cy="6" r="5" fill="#222"/></svg>
    <div class="name">Online Access!</div><div class="sub">Click here for client access</div>
  </div>

  <h2 class="abs sec-title" style="left:146px;top:923px;width:292px">Debt Collection &amp; Debt Recovery</h2>
  <div class="abs body-text" style="left:148px;top:965px;width:510px">
    Lorem Ipsum is simply dummy text of the printing and typesetting industry. Lorem Ipsum has been the industry's standard dummy text ever since the 1500s, when an unknown printer took a galley of type and scrambled it to make a type specimen book. It has survived not only five centuries, but also the leap into electronic typesetting, remaining essentially unchanged. It was popularised in the 1960s with the release of Letraset sheets containing Lorem Ipsum passages, and more recently with desktop publishing software like Aldus PageMaker including versions of Lorem Ipsum.
  </div>
</main>

<aside>
  <h2 class="abs sec-title" style="left:690px;top:318px;width:136px">Meridian News</h2>
  <div class="abs body-text" style="left:691px;top:360px;width:205px">
    Lorem Ipsum is simply dummy text of the printing and typesetting industry. Lorem Ipsum has been the industry's standard dummy text ever since the 1500s, when an unknown printer took a galley of type and scrambled it to make a type specimen book.
  </div>
  <div class="abs photo-card" role="img" aria-label="Office team reviewing documents beside payment card panel">
    <div class="caption">Ledgerwise</div>
  </div>
  <div class="abs promo" role="img" aria-label="Portrait of smiling businesswoman">
    <div class="lines"><div class="l1">Recommend our service</div><div class="l2">Earn free gift vouchers</div></div>
  </div>
</aside>

<footer>
  <div class="abs footer-rule"></div>
  <nav class="abs footer-nav"><span>Home</span><span>About</span><span>Rates</span><span>Products &amp; Solutions</span><span>Media Centre</span><span>Careers</span><span>Contact us</span><span>Client Login</span></nav>
  <div class="abs copyright">Copyright © Tolvane Fast Debt Recovery Pty Ltd 2011 All Rights Reserved</div>
</footer>

</body>
</html>
```